Onlineshop für hochwertige Gebrauchtsättel für den Reitsport sucht Webdesign
Zielgruppe
Wir verkaufen hochwertige Gebrauchtsättel für den Reitsport und möchten Reiter jeder Altersgruppe ansprechen.
Aufgabenstellung
Farbgebung : grün braun (eventuell gelb), naturnahe Farben
Ein Logo ist bereits vorhanden.

```html
<!DOCTYPE html>
<html lang="de">
<head>
<meta charset="utf-8">
<title>The Oakstirrup – Gebrauchtsättel</title>
<link href="https://fonts.googleapis.com/css2?family=Merriweather:wght@300;400&family=Open+Sans:wght@300;400;600&display=swap" rel="stylesheet">
<style>
:root{
  --brown:#6b4320;
  --brown-text:#7a5233;
  --green:#8cc63f;
  --ink:#333;
  --grey:#777;
  --tile:#e3e5e7;
  --line:#b9b1a8;
}
*{margin:0;padding:0;box-sizing:border-box}
html,body{width:1200px;height:3593px;overflow:hidden;background:#fff}
body{position:relative;font-family:'Open Sans',sans-serif;color:var(--ink)}
.abs{position:absolute}
.hero{left:0;top:0;width:1200px;height:677px;background:radial-gradient(ellipse at 25% 45%,#fff 0%,#f3f3f4 45%,#dcdde0 100%)}
.brand{left:118px;top:250px;width:196px;text-align:center;font-family:'Merriweather',serif;font-size:19px;color:var(--brown-text);letter-spacing:1px}
.brand-mark{left:192px;top:184px;width:50px;height:50px;border-radius:50%;background:var(--green)}
.hero-title{left:95px;top:352px;font-weight:300;font-size:41px;line-height:48px;color:#333;letter-spacing:.3px}
.nav{left:95px;top:522px;display:flex;gap:30px;font-family:'Merriweather',serif;font-size:19px;color:var(--brown-text)}
.nav a{color:inherit;text-decoration:none;padding-bottom:12px}
.nav a.active{border-bottom:2px solid var(--brown-text)}
.hero-photo{left:607px;top:42px;width:481px;height:635px;border-radius:40% 30% 8% 20%;background:radial-gradient(ellipse at 55% 45%,#3a3633 0%,#24211f 55%,#4a2c22 100%)}
.intro-title{left:95px;top:745px;font-weight:300;font-size:26px;line-height:33px;color:#333}
.intro-text{left:95px;top:855px;width:340px;font-family:'Merriweather',serif;font-weight:300;font-size:16px;line-height:26px;color:var(--brown-text)}
.btn{display:flex;align-items:center;justify-content:center;border-radius:22px;color:#fff;font-size:12px;font-weight:600;text-transform:uppercase;letter-spacing:.3px}
.btn-brown{background:var(--brown)}
.popup{left:924px;top:749px;width:276px;height:276px;background:#fff;box-shadow:0 4px 18px rgba(0,0,0,.25)}
.popup .avatar{position:absolute;left:106px;top:30px;width:64px;height:64px;border-radius:50%;background:radial-gradient(circle,#e9cfa6,#c89a63)}
.popup .msg{position:absolute;left:0;top:112px;width:276px;text-align:center;font-size:14px;line-height:18px;text-transform:uppercase;color:#333}
.popup .contact{position:absolute;left:44px;top:200px;font-family:'Merriweather',serif;font-size:13px;color:var(--brown-text);line-height:24px}
.popup .contact div{display:flex;align-items:center;gap:10px}
.tile{width:264px;height:264px;overflow:hidden}
.tile-photo{width:100%;height:100%}
.tile .arrow{position:absolute;right:0;bottom:0;width:44px;height:44px;background:#111}
.bg-wall{background:linear-gradient(180deg,#8a7a62 0%,#3c3632 40%,#2a2624 70%,#5a4c3a 100%)}
.bg-green{background:linear-gradient(180deg,#3e6a2a 0%,#2a2624 45%,#2d2a28 70%,#4f7a38 100%)}
.bg-studio{background:radial-gradient(ellipse at 50% 50%,#2b2826 0%,#2b2826 35%,#e8e9eb 60%,#f2f2f3 100%)}
.bg-brown-green{background:linear-gradient(180deg,#4e7a34 0%,#5a2e24 40%,#4a2820 70%,#5c7d3c 100%)}
.bg-brown-studio{background:radial-gradient(ellipse at 50% 50%,#5a3222 0%,#5a3222 35%,#e4e5e7 62%,#f0f0f1 100%)}
.bg-brown-wall{background:linear-gradient(180deg,#756a58 0%,#4a2c24 40%,#3e2620 70%,#6b6048 100%)}
.tile-info{background:var(--tile);text-align:center;font-family:'Merriweather',serif;color:#333}
.tile-info .name{position:absolute;left:20px;top:70px;width:224px;font-size:16px;line-height:22px}
.tile-info .price{position:absolute;left:0;top:178px;width:264px;font-size:22px;color:var(--brown-text)}
.contact-section{left:0;top:2497px;width:1200px;height:579px;background:radial-gradient(ellipse at 50% 40%,#fbfaf8 0%,#f1efec 70%,#e8e5e0 100%)}
.contact-title{left:0;top:2595px;width:1200px;text-align:center;font-weight:300;font-size:26px;line-height:33px;color:#333}
.person{left:254px;top:2723px;width:156px;height:156px;border-radius:50%;background:radial-gradient(circle,#f0dcc0,#caa06a)}
.person-info{left:200px;top:2905px;width:264px;text-align:center;font-family:'Merriweather',serif;font-size:16px;line-height:26px;color:var(--brown-text)}
.divider{left:481px;top:2723px;width:1px;height:255px;background:var(--line)}
.field{border-bottom:1px solid var(--line);font-family:'Merriweather',serif;font-size:14px;color:var(--grey);padding-bottom:12px}
.btn-green{background:var(--green)}
.band{left:0;top:3076px;width:1200px;height:321px;background:linear-gradient(180deg,#e4e6e9 0%,#d7d9dc 100%)}
.band-photo{left:230px;top:3076px;width:760px;height:321px;border-radius:40% 40% 0 0;background:radial-gradient(ellipse at 50% 60%,#2c2a28 0%,#1d1b1a 60%,#3a3532 100%)}
.footer h4{font-family:'Merriweather',serif;font-weight:400;font-size:19px;color:var(--brown-text);text-transform:uppercase;margin-bottom:18px}
.footer p{font-size:14px;color:var(--brown-text);line-height:33px;display:flex;align-items:center;gap:8px}
.sq{width:24px;height:24px;background:var(--brown)}
.footer-brand{left:950px;top:3530px;width:210px;text-align:center;font-family:'Merriweather',serif;font-size:21px;color:var(--brown-text);letter-spacing:1px}
.footer-mark{left:1025px;top:3440px;width:60px;height:60px;border-radius:50%;background:var(--green)}
</style>
</head>
<body>

<section class="abs hero"></section>
<div class="abs brand-mark"></div>
<div class="abs brand">THE OAKSTIRRUP</div>
<h1 class="abs hero-title">WÄHLE AUS EINER BREITEN<br>PALETTE GEBRAUCHTER<br>SÄTTEL DEINEN FAVORITEN</h1>
<nav class="abs nav">
  <a class="active">Gebrauchtsättel</a><a>Preisliste</a><a>Über uns</a><a>Kontakt</a>
</nav>
<div class="abs hero-photo" role="img" aria-label="Foto eines schwarzen Dressursattels"></div>

<h2 class="abs intro-title" style="font-weight:300">HIER FINDEST DU SÄTTEL, DIE<br>WIR IN UNSEREM AKTUELLEN<br>SORTIMENT HABEN.</h2>
<p class="abs intro-text">Wir haben nur solche Sättel in unserem Sortiment, deren Passform uns überzeugt und die wir selbst auf unseren Pferden nutzen würden.</p>
<div class="abs btn btn-brown" style="left:95px;top:976px;width:300px;height:43px">Bereits verkaufte Sättel ansehen</div>

<aside class="abs popup">
  <svg class="abs" style="left:240px;top:14px" width="22" height="22" viewBox="0 0 22 22"><path d="M2 2L20 20M20 2L2 20" stroke="#666" stroke-width="1.5"/></svg>
  <div class="avatar" role="img" aria-label="Porträtfoto der Ansprechpartnerin"></div>
  <div class="msg">Du möchtest einen<br>Sattel bestellen oder<br>hast Fragen? Wir sind<br>gerne für dich da!</div>
  <div class="contact">
    <div><svg width="16" height="12" viewBox="0 0 16 12"><rect width="16" height="12" fill="#6b4320"/><path d="M0 0L8 7L16 0" stroke="#fff" fill="none"/></svg>lena@oakstirrup.de</div>
    <div><svg width="16" height="16" viewBox="0 0 16 16"><path d="M3 1l3 3-2 2c1 2 3 4 5 5l2-2 3 3-2 3C7 15 1 9 1 3z" fill="#6b4320"/></svg>0176 55512048</div>
  </div>
</aside>

<div class="abs tile" style="left:153px;top:1099px"><div class="tile-photo bg-wall" role="img" aria-label="Schwarzer Sattel vor Steinmauer"></div><div class="arrow"><svg width="44" height="44"><path d="M18 12l10 10-10 10" stroke="#fff" stroke-width="2" fill="none"/></svg></div></div>
<div class="abs tile" style="left:467px;top:1099px"><div class="tile-photo bg-green" role="img" aria-label="Schwarzer Sattel vor Grün"></div><div class="arrow"><svg width="44" height="44"><path d="M18 12l10 10-10 10" stroke="#fff" stroke-width="2" fill="none"/></svg></div></div>
<div class="abs tile" style="left:782px;top:1099px"><div class="tile-photo bg-studio" role="img" aria-label="Schwarzer Sattel im Studio"></div><div class="arrow"><svg width="44" height="44"><path d="M18 12l10 10-10 10" stroke="#fff" stroke-width="2" fill="none"/></svg></div></div>

<div class="abs tile" style="left:153px;top:1412px"><div class="tile-photo bg-green" role="img" aria-label="Schwarzer Dressursattel vor Grün"></div><div class="arrow"><svg width="44" height="44"><path d="M18 12l10 10-10 10" stroke="#fff" stroke-width="2" fill="none"/></svg></div></div>
<div class="abs tile tile-info" style="left:467px;top:1412px">
  <svg class="abs" style="left:222px;top:16px" width="22" height="22"><path d="M2 2L20 20M20 2L2 20" stroke="#666" stroke-width="1.5"/></svg>
  <div class="name">Reitwerk Selene Dressursattel Bananenkissen ultra kurz 17,5 Zoll</div>
  <div class="price">899 €</div>
</div>
<div class="abs tile" style="left:782px;top:1412px"><div class="tile-photo bg-wall" role="img" aria-label="Schwarzer Sattel vor Steinmauer"></div><div class="arrow"><svg width="44" height="44"><path d="M18 12l10 10-10 10" stroke="#fff" stroke-width="2" fill="none"/></svg></div></div>

<div class="abs tile" style="left:153px;top:1724px"><div class="tile-photo bg-green" role="img" aria-label="Schwarzer Sattel vor Grün"></div><div class="arrow"><svg width="44" height="44"><path d="M18 12l10 10-10 10" stroke="#fff" stroke-width="2" fill="none"/></svg></div></div>
<div class="abs tile" style="left:467px;top:1724px"><div class="tile-photo bg-brown-green" role="img" aria-label="Brauner Sattel vor Grün"></div><div class="arrow"><svg width="44" height="44"><path d="M18 12l10 10-10 10" stroke="#fff" stroke-width="2" fill="none"/></svg></div></div>
<div class="abs tile" style="left:782px;top:1724px"><div class="tile-photo bg-brown-studio" role="img" aria-label="Brauner Sattel im Studio"></div><div class="arrow"><svg width="44" height="44"><path d="M18 12l10 10-10 10" stroke="#fff" stroke-width="2" fill="none"/></svg></div></div>

<div class="abs tile" style="left:153px;top:2037px"><div class="tile-photo bg-wall" role="img" aria-label="Schwarzer Springsattel vor Steinmauer"></div><div class="arrow"><svg width="44" height="44"><path d="M18 12l10 10-10 10" stroke="#fff" stroke-width="2" fill="none"/></svg></div></div>
<div class="abs tile" style="left:467px;top:2037px"><div class="tile-photo bg-brown-studio" role="img" aria-label="Hellbrauner Sattel im Studio"></div><div class="arrow"><svg width="44" height="44"><path d="M18 12l10 10-10 10" stroke="#fff" stroke-width="2" fill="none"/></svg></div></div>
<div class="abs tile" style="left:782px;top:2037px"><div class="tile-photo bg-brown-wall" role="img" aria-label="Dunkelbrauner Sattel auf Holzbalken"></div><div class="arrow"><svg width="44" height="44"><path d="M18 12l10 10-10 10" stroke="#fff" stroke-width="2" fill="none"/></svg></div></div>

<div class="abs btn btn-brown" style="left:467px;top:2370px;width:264px;height:44px">Weitere Sättel anzeigen</div>

<section class="abs contact-section" role="img" aria-label="Heller Hintergrund mit Pferdemähne"></section>
<h2 class="abs contact-title" style="font-weight:300">NIMM KONTAKT ZU UNS AUF. WIR<br>FREUEN UNS AUF DICH!</h2>
<div class="abs person" role="img" aria-label="Porträtfoto von Lena Hartwig"></div>
<div class="abs person-info">Lena Hartwig<br>0176 55512048<br>lena@oakstirrup.de</div>
<div class="abs divider"></div>
<div class="abs field" style="left:547px;top:2723px;width:196px">Name</div>
<div class="abs field" style="left:777px;top:2723px;width:196px">E-Mail-Adresse</div>
<div class="abs field" style="left:547px;top:2799px;width:426px">Betreff</div>
<div class="abs field" style="left:547px;top:2876px;width:426px">Nachricht</div>
<div class="abs btn btn-green" style="left:615px;top:2932px;width:290px;height:44px">Senden</div>

<div class="abs band"></div>
<div class="abs band-photo" role="img" aria-label="Nahaufnahme eines schwarzen Ledersattels"></div>

<footer class="footer">
  <div class="abs" style="left:62px;top:3430px"><h4>The Oakstirrup</h4><p>Lena Hartwig</p><p>Gut am Wiesenrain</p><p>64300 Lindenfeld</p></div>
  <div class="abs" style="left:336px;top:3430px"><h4>Kontakt</h4><p>lena@oakstirrup.de</p><p>0176 55512048</p><p><span class="sq"></span>follow me</p></div>
  <div class="abs" style="left:607px;top:3430px"><h4>Rechtliches</h4><p>AGB</p><p>Impressum</p><p>Datenschutz</p></div>
  <div class="abs footer-mark"></div>
  <div class="abs footer-brand">THE OAKSTIRRUP</div>
</footer>

</body>
</html>
```